Business Card - high end, modern health care

Hey designers!

We need a double sided business card for the boutique, cutting edge physical therapy rehabilitation centre in Sydney's Northern Beaches.

With the most qualified physios in the area The Harbourline Motion Clinic does what other physiotherapy practices do not, we take our time with our patients giving them longer appointments, better physios and therefor faster results!

We guarantee that the service people receive at THMC will be unparalleled.

Hence we need a business card to reflect our modern, boutique, high end service. The final design needs to reflect that we are in a class of our own yet with the feel of beachside retreat.

Below I have attached our logo in both blue on white and white on blue. The exact colour is;
and the font that we have used in our logo is Tex Gyre Aventador.

I like the idea of the blue as the main colour as it is more eye catching and our signage onto the main road will be in this blue and in the interest of consistency across marketing the blue needs to be a part of the design. However I would appreciate a few designs onto a wooden background as this is a visual theme within the fitout of the practice.

The design needs to be of standard size (91x55mm).

Target Market(s)

We target people who have an end outcome in mind and those who have had poor experiences with other providers and ensure that everyone gets the care that they deserve with a premium service that is tailored to the individuals circumstances. As a premium service, the target market is highly educated, business and tech savvy with the additional target market of elderly people who have self funded their retirement and see value in paying for the best ongoing rehabilitation to maintain independence.

Industry/Entity Type

Physical Therapy

Contact Information for Business Card

Name, designation( Titled Musculoskeletal Physiotherapist... there will also be those in the company that have multiple designations ie 5 or 6 words long), phone number, email, facebook, instagram, address

Font styles to use
Sans Serif

Colors

Designer to choose colors to be used in the design.

Requirements
Must have
• Front - The logo as large as possible, blue or wooden theme, and all of the important details.
• Back - A blank space/lines on which to write appointment times (no "Appointment, date, time" etc.)
Nice to have
• facebook url
• logos for facebook and instagram
• Mini logos for the phone and email?

```html
<!DOCTYPE html>
<html lang="en">
<head>
<meta charset="utf-8">
<title>The Harbourline Motion Clinic – Business Card</title>
<link href="https://fonts.googleapis.com/css2?family=Questrial&family=Roboto+Condensed:wght@400;700&display=swap" rel="stylesheet">
<style>
  :root {
    --stage: #2a2b2f;
    --navy: #141646;
    --navy-deep: #10123b;
    --blue: #0a62bd;
    --paper: #dcdde2;
    --dots: #1b1d4f;
  }
  * { box-sizing: border-box; margin: 0; padding: 0; }
  html, body { width: 1200px; height: 900px; overflow: hidden; }
  body {
    background: var(--stage);
    font-family: "Roboto Condensed", "Arial Narrow", sans-serif;
    position: relative;
  }
  .card {
    position: absolute;
    width: 560px;
    height: 338px;
    background: var(--navy);
    overflow: hidden;
    box-shadow: 0 14px 30px rgba(0,0,0,.45);
  }
  .card--back { left: 320px; top: 70px; }
  .card--front { left: 320px; top: 470px; }

  .edge-tab { position: absolute; background: var(--blue); }

  /* brand lockup */
  .brand { position: absolute; display: flex; align-items: center; gap: 12px; }
  .brand__mark {
    width: 44px; height: 44px; border-radius: 50%;
    background: var(--blue); flex: none;
  }
  .brand__name {
    font-family: "Questrial", sans-serif;
    color: var(--blue);
    font-size: 19px;
    letter-spacing: .06em;
    text-transform: uppercase;
    line-height: 1.15;
  }

  /* back side */
  .card--back .brand { right: 40px; top: 60px; }
  .appointment-band {
    position: absolute; left: 0; right: 0; top: 168px; height: 112px;
    background: var(--blue); padding: 10px 0;
  }
  .appointment-band__paper {
    height: 100%; background: var(--paper);
    padding: 18px 34px 0;
    position: relative;
  }
  .write-line {
    border-bottom: 2px dotted var(--dots);
    height: 22px;
  }
  .appointment-band__label {
    position: absolute; right: 34px; bottom: 10px;
    font-weight: 700; font-size: 15px; color: var(--navy);
  }

  /* front side */
  .card--front .brand { left: 32px; top: 34px; }
  .address {
    position: absolute; left: 32px; top: 120px;
    color: var(--blue); font-size: 14px; line-height: 1.35;
  }
  .person { position: absolute; right: 32px; top: 120px; text-align: right; }
  .person__name {
    color: var(--blue); font-weight: 700; font-size: 26px;
    text-transform: uppercase; letter-spacing: .01em;
  }
  .person__title { color: var(--blue); font-size: 14px; }
  .therapy-pictograms {
    position: absolute; left: 200px; top: 196px;
    width: 120px; height: 92px;
  }
  .contacts {
    position: absolute; right: 32px; top: 186px;
    list-style: none; text-align: right;
  }
  .contacts li {
    display: flex; justify-content: flex-end; align-items: center; gap: 8px;
    color: var(--blue); font-size: 14px; height: 26px;
  }
  .contacts .icon {
    width: 18px; height: 18px; background: var(--blue); border-radius: 3px;
    display: flex; align-items: center; justify-content: center; flex: none;
  }
</style>
</head>
<body>

  <section class="card card--back" aria-label="Card back">
    <div class="edge-tab" style="left:0;top:0;width:34px;height:8px"></div>
    <div class="edge-tab" style="right:0;top:0;width:8px;height:34px"></div>
    <div class="brand">
      <span class="brand__mark"></span>
      <span class="brand__name">The Harbourline<br>Motion Clinic</span>
    </div>
    <div class="appointment-band">
      <div class="appointment-band__paper">
        <div class="write-line"></div>
        <div class="write-line"></div>
        <span class="appointment-band__label">Appointment Times</span>
      </div>
    </div>
  </section>

  <section class="card card--front" aria-label="Card front">
    <div class="edge-tab" style="left:0;top:70px;width:8px;height:30px"></div>
    <div class="edge-tab" style="right:0;top:210px;width:8px;height:40px"></div>

    <div class="brand">
      <span class="brand__mark"></span>
      <span class="brand__name">The Harbourline<br>Motion Clinic</span>
    </div>

    <p class="address">PO Box 4410 | 18 Pittwater Road<br>Dee Why, NSW, Australia</p>

    <div class="person">
      <h1 class="person__name">Daniel Carrow</h1>
      <p class="person__title">Musculoskeletal Physiotherapist</p>
    </div>

    <svg class="therapy-pictograms" role="img" aria-label="Pictograms of a runner and hands-on physiotherapy treatment" viewBox="0 0 120 92">
      <rect width="120" height="92" rx="6" fill="#0a62bd" opacity=".35"/>
    </svg>

    <ul class="contacts">
      <li>+61 2 5550 0147
        <span class="icon"><svg width="12" height="12" viewBox="0 0 24 24"><path fill="#141646" d="M6.6 10.8a15 15 0 0 0 6.6 6.6l2.2-2.2c.3-.3.7-.4 1-.2 1.1.4 2.3.6 3.6.6.6 0 1 .4 1 1V20c0 .6-.4 1-1 1A17 17 0 0 1 3 4c0-.6.4-1 1-1h3.5c.6 0 1 .4 1 1 0 1.3.2 2.5.6 3.6.1.3 0 .7-.2 1z"/></svg></span>
      </li>
      <li>hello@harbourlinemotion.com
        <span class="icon"><svg width="12" height="12" viewBox="0 0 24 24"><path fill="none" stroke="#141646" stroke-width="2.4" d="M3 6h18v12H3zM3 6l9 7 9-7"/></svg></span>
      </li>
      <li>Facebook/HarbourlineMotion <span class="icon"></span></li>
      <li>@harbourlinemotion <span class="icon"></span></li>
    </ul>
  </section>

</body>
</html>
```